Save our Business Card - We need your help

We need a fresh look on our business cards. We like it as it is, but it's not quite getting the 'wow' effect that we desire.
We're a tech startup building a cloud based solution for retailers consisting of Point of Sale, Inventory management and CRM.
The design should communicate a sense of a company that cares about the little things, design and relationships.
You can have a look at our website www.tillnest.com to get a feel for what we're like. Please feel free to message us for any further clarification
Target Market(s)
Our Customers are retail busines owners, cafe owners, other startups etc.
Industry/Entity Type
Building
Colors
Designer to choose colors to be used in the design.
Look and feel
Each slider illustrates characteristics of the customer's brand and the style your logo design should communicate.

```html
<!DOCTYPE html>
<html lang="en">
<head>
<meta charset="utf-8">
<title>Tillnest – Enterprise Features for Everyone</title>
<link href="https://fonts.googleapis.com/css2?family=Roboto:wght@700&family=Source+Sans+3:wght@400;700&display=swap" rel="stylesheet">
<style>
  :root {
    --brand-orange: #f5821f;
    --text-light: #ececec;
    --bg-glow: #2b2b2b;
    --bg-mid: #141414;
    --bg-edge: #000000;
  }
  html, body {
    margin: 0;
    padding: 0;
    overflow: hidden;
    background: var(--bg-edge);
  }
  .card {
    position: relative;
    width: 1200px;
    height: 702px;
    overflow: hidden;
    background: radial-gradient(ellipse 70% 85% at 52% 62%, var(--bg-glow) 0%, var(--bg-mid) 55%, var(--bg-edge) 100%);
  }
  .headline {
    position: absolute;
    left: 310px;
    top: 96px;
    margin: 0;
    font-family: "Roboto", Arial, sans-serif;
    font-weight: 700;
    font-size: 34px;
    letter-spacing: 0.2px;
    color: var(--brand-orange);
  }
  .feature-list {
    position: absolute;
    left: 396px;
    top: 166px;
    margin: 0;
    padding: 0;
    list-style: none;
    font-family: "Source Sans 3", "Myriad Pro", sans-serif;
    font-weight: 400;
    font-size: 33px;
    line-height: 50.8px;
    color: var(--text-light);
  }
  .feature-list li {
    position: relative;
    padding-left: 26px;
  }
  .feature-list li::before {
    content: "";
    position: absolute;
    left: 0;
    top: 23px;
    width: 6px;
    height: 6px;
    border-radius: 50%;
    background: var(--text-light);
  }
  .brand {
    position: absolute;
    left: 74px;
    top: 576px;
    display: flex;
    align-items: center;
    gap: 14px;
  }
  .brand-square {
    width: 56px;
    height: 56px;
    background: var(--brand-orange);
  }
  .brand-name {
    font-family: "Source Sans 3", "Myriad Pro", sans-serif;
    font-weight: 700;
    font-size: 50px;
    line-height: 1;
    color: var(--brand-orange);
  }
</style>
</head>
<body>
  <main class="card">
    <h1 class="headline">Enterprise Features for Everyone</h1>
    <ul class="feature-list">
      <li>Real-Time Reports</li>
      <li>Offline Protection</li>
      <li>Inventory Management</li>
      <li>Employee Timesheets</li>
      <li>Customer Relationship Management</li>
      <li>Free &amp; Automatic Updates</li>
      <li>Unlimited Phone/Email Support</li>
    </ul>
    <div class="brand">
      <span class="brand-square" aria-hidden="true"></span>
      <span class="brand-name">Tillnest</span>
    </div>
  </main>
</body>
</html>
```